A new fresh and flat K&T Logistics Brochure Design A4 - 4 pages

Our client is an established International Logistics firm looking to upgrade their sales brochure.
We would like the designer to create concepts that are flat, modern and communicate reliability and expediency to our clients. We want the brochure to maintain a degree of white space and minimal design.
Introduction
LOGISTICS - it's what we do best! We're proud to say so after 27 years (and counting) of organic growth within the 3PL industry. Starting off in Meridian, Mississippi with a fleet of 4 trucks in 1987, K&T is today a global 3PL company with offices in the United States and Asia Pacific region.
Our goal has always been to serve our clients by getting things done, and getting them done right.
Format: A4 4-sided brochure
Pg 1 Front Page - Company name and logo, and vector design concept to make front page unique. Please try to include some kind of container reference design on the front page (e.g 2D or 3D vector, transparent overlay etc...), place this design element somewhere in the middle or bttom of the page.
Pg 2 and/or Pg 3
- Introduction and Core services Including: ABOUT, SERVICES, CONTRACT LOGISTICS, K&T INTEL (following the menu content of our website www.ktvrx.example)
- Text space to explain Services in more detail.
Social proof (existing client testimonials/feedback.)
- A 'C.A.R.E' acronym design element, including the words: Communicative, Accessible, Responsible, Efficient
Pg 4 Back Page- Contact information, Call to action.
Throughut the brochure please leave space for images as you deem appropriate and we will update late OR even better usesome of your own stock images.
Color theme: Based on corporate colors (but not limited to), see website
http://www.ktvrx.example
Try diffent font types to the website both serif and sans serif
Include several CTAs throughout the brochure.
You can use both the attached pdf brochure and the website for content.
We would also appreciate if you could also enhance the logo to make it 'pop' (keep shape and style).

```html
<!DOCTYPE html>
<html lang="en">
<head>
<meta charset="utf-8">
<title>K&amp;T Logistics – Company Introduction</title>
<link rel="stylesheet" href="https://fonts.googleapis.com/css2?family=Lato:wght@300;400;700&family=Ubuntu:wght@400;500;700&family=Roboto:wght@400&display=swap">
<style>
  :root {
    --slate: #4a6479;
    --panel-grey: #e4e5e7;
    --page-white: #f7f8f9;
    --ink: #1d1d1d;
    --brand-blue: #2a5a7e;
    --watermark: rgba(255,255,255,0.3);
  }
  * { margin: 0; padding: 0; box-sizing: border-box; }
  html, body { width: 1200px; height: 1000px; overflow: hidden; background: #ffffff; }
  body { position: relative; font-family: "Ubuntu", Arial, sans-serif; color: var(--ink); }

  .spread {
    position: absolute; left: 35px; top: 102px; width: 1140px; height: 808px;
    background: var(--page-white);
    box-shadow: 0 4px 14px rgba(0,0,0,0.35);
    overflow: hidden;
  }
  .inner-panel {
    position: absolute; left: 0; top: 0; width: 568px; height: 643px;
    background: var(--panel-grey);
  }
  .cover-panel {
    position: absolute; left: 568px; top: 0; width: 572px; height: 643px;
    background: linear-gradient(#eceef0, #ffffff 30%);
  }

  .watermark-clip {
    position: absolute; left: 0; top: 370px; width: 568px; height: 438px;
    overflow: hidden; z-index: 1; pointer-events: none;
  }
  .watermark-name {
    position: absolute; left: 20px; top: 10px;
    font-family: "Ubuntu", sans-serif; font-weight: 700; font-size: 400px; line-height: 1;
    color: var(--watermark); letter-spacing: -14px; white-space: nowrap;
  }

  .section-title { font-family: "Lato", sans-serif; font-weight: 300; color: var(--slate); }
  .about { position: absolute; left: 25px; top: 20px; width: 515px; z-index: 2; }
  .about .section-title { font-size: 29px; line-height: 1.1; margin-bottom: 2px; }
  .about p { font-size: 9.6px; line-height: 1.33; margin-bottom: 11px; }

  .mission {
    position: absolute; left: 25px; top: 215px; width: 527px; height: 91px;
    background: var(--slate); color: #fff; padding: 4px 10px; z-index: 2;
  }
  .mission .section-title { color: #fff; font-size: 29px; line-height: 1.1; margin-bottom: 4px; }
  .mission p { font-size: 9.6px; line-height: 1.33; }

  .offices-label {
    position: absolute; left: 175px; top: 481px; width: 216px; height: 24px; z-index: 2;
    background: var(--slate); border-radius: 12px; color: #fff;
    font-weight: 700; font-size: 17px; text-align: center; line-height: 24px; letter-spacing: 0.3px;
  }
  .office {
    position: absolute; top: 538px; width: 200px; text-align: center; z-index: 2;
    font-size: 10.8px; line-height: 1.22;
  }
  .office h3 { color: var(--slate); font-size: 17px; font-weight: 700; margin-bottom: 9px; }
  .office-china { left: 3px; }
  .office-usa { left: 185px; }
  .office-hk { left: 365px; }

  .brand-name {
    position: absolute; left: 633px; top: 40px;
    font-family: "Ubuntu", sans-serif; font-weight: 700; font-size: 62px; line-height: 1;
    color: var(--brand-blue);
  }
  .brand-tagline {
    position: absolute; left: 757px; top: 91px;
    font-family: "Ubuntu", sans-serif; font-weight: 700; font-size: 17px; color: var(--brand-blue);
  }

  .tile { position: absolute; width: 173px; height: 156px; border-radius: 12px; }
  .tile-a { background: linear-gradient(135deg, #c5d3e0, #7f99b2); }
  .tile-b { background: linear-gradient(160deg, #b9c9d8, #55718d 70%); }
  .tile-c { background: linear-gradient(200deg, #9fb6cb, #c9d6e3 60%, #a2b6c9); }
  .tile-d { background: linear-gradient(170deg, #8ea6bd, #c4d1dd 50%, #6c87a1); }
  .tile-e { background: linear-gradient(180deg, #a8bccf, #5c7892); }
  .tile-f { background: linear-gradient(180deg, #b2c4d5, #5a7590); }
  .tile-g { background: linear-gradient(150deg, #5f7b96, #8ba3ba 60%, #3f5c78); }
  .tile-h { background: linear-gradient(180deg, #6f8aa4, #3f5c78); }
  .tile-i { background: linear-gradient(180deg, #8ca3b9, #4b6782); }

  .footer-band {
    position: absolute; left: 0; top: 643px; width: 1140px; height: 165px;
    background: var(--slate);
  }
  .footer-band::before {
    content: ""; position: absolute; left: 0; top: 5px; width: 100%; height: 2px; background: #ffffff;
  }
  .contact-list { position: absolute; left: 328px; top: 24px; z-index: 2; color: #fff; font-family: "Roboto", Arial, sans-serif; font-size: 13.5px; line-height: 19px; }
  .contact-row { position: relative; padding-left: 36px; margin-bottom: 6px; }
  .contact-row svg { position: absolute; left: 0; top: 1px; }
  .title-block { position: absolute; right: 30px; top: 20px; z-index: 2; text-align: right; color: #fff; font-family: "Lato", sans-serif; }
  .title-light { font-weight: 300; font-size: 41px; letter-spacing: 1px; line-height: 1.2; }
  .title-bold { font-weight: 700; font-size: 44px; line-height: 1.2; }
</style>
</head>
<body>
<main class="spread">
  <section class="inner-panel">
    <article class="about">
      <h2 class="section-title">About Us</h2>
      <p>With roots in the US Road Transportation Industry, K&amp;T has evolved over the last 25 years from being a regional road transportation company to a global provider of leading, innovative, and fully integrated supply chain logistics and management.</p>
      <p>Founded in Meridian, MS in 1987, K&amp;T began its business in the road transportation industry. With a fleet of over 30 trucks servicing the greater American South East, K&amp;T has expanded its base over the years to evolve into a provider of International Road, Rail, Sea and Air transportation.</p>
      <p>The rapid development of global trade over the last decade has also seen K&amp;T specialize in 3PL and<br>4PL management of warehousing and distribution, customs brokerage, and industry specific supply chain consulting. Today K&amp;T has offices in the Greater United States and Asia Pacific region as well as a worldwide network of trusted partners that ensure we are globally present to serve our clients requirements.</p>
    </article>

    <article class="mission">
      <h2 class="section-title">Mission Statement</h2>
      <p>Customer focus,innovation,and operational excellence are the driving forces behind our aim to provide fully integrated logistics solutions. Dedication,quality of service,and the expertise of our personnel are the asset base we draw upon to strive to be not just a partner,but an extension of our clients' business</p>
    </article>

    <div class="offices-label">OUR OFFICES</div>
    <div class="office office-china">
      <h3>CHINA</h3>
      K&amp;T Logistics<br>18F, Harbour Point Tower, Bay Road,<br>Nanshan District, Shenzhen 518000,<br><strong>Telephone: +86 755 2000 0147</strong>
    </div>
    <div class="office office-usa">
      <h3>USA</h3>
      K&amp;T Transport<br>2150 Riverbend Parkway<br>Meridian, MS 39301 USA<br><strong>Telephone: +1 601 555 0186</strong>
    </div>
    <div class="office office-hk">
      <h3>HONG KONG</h3>
      K&amp;T Logistics<br>12F Harbourline Centre<br>88 Queensway Road, Central,<br><strong>Telephone: +852 8100 0293</strong>
    </div>
  </section>

  <section class="cover-panel"></section>

  <div class="brand-name">K&amp;T</div>
  <div class="brand-tagline">Logistics and Supply Chain Solutions</div>

  <div class="tile tile-a" style="left:587px;top:150px" role="img" aria-label="Photo of stacked shipping containers"></div>
  <div class="tile tile-b" style="left:767px;top:150px" role="img" aria-label="Photo of a container crane stairway"></div>
  <div class="tile tile-c" style="left:946px;top:150px" role="img" aria-label="Photo of containers lifted by crane"></div>
  <div class="tile tile-d" style="left:587px;top:312px" role="img" aria-label="Photo of a container truck on the road"></div>
  <div class="tile tile-e" style="left:767px;top:312px" role="img" aria-label="Photo of a container port yard"></div>
  <div class="tile tile-f" style="left:946px;top:312px" role="img" aria-label="Photo of port straddle carriers"></div>
  <div class="tile tile-g" style="left:587px;top:474px" role="img" aria-label="Photo of rows of containers in a terminal"></div>
  <div class="tile tile-h" style="left:767px;top:474px" role="img" aria-label="Photo of container stacks at a terminal"></div>
  <div class="tile tile-i" style="left:946px;top:474px" role="img" aria-label="Photo of a straddle carrier moving containers"></div>

  <footer class="footer-band">
    <div class="contact-list">
      <div class="contact-row">
        <svg width="22" height="24" viewBox="0 0 22 24" aria-hidden="true">
          <rect x="1" y="3" width="20" height="19" rx="2" fill="#fff"/>
          <rect x="3" y="1" width="5" height="21" rx="1.5" fill="#fff" stroke="#4a6479" stroke-width="1"/>
          <g fill="#4a6479"><rect x="10" y="6" width="9" height="3"/><rect x="10" y="11" width="2" height="2"/><rect x="13.5" y="11" width="2" height="2"/><rect x="17" y="11" width="2" height="2"/><rect x="10" y="15" width="2" height="2"/><rect x="13.5" y="15" width="2" height="2"/><rect x="17" y="15" width="2" height="2"/></g>
        </svg>
        +1 (601) 555 0186 (US)<br>+86 (755) 2000 0147 (Asia)<br>+852 8100 0293 (HK)
      </div>
      <div class="contact-row">
        <svg width="22" height="20" viewBox="0 0 22 20" aria-hidden="true">
          <rect x="1" y="5" width="20" height="14" fill="#fff"/>
          <polyline points="1,5 11,13 21,5" fill="none" stroke="#4a6479" stroke-width="1.5"/>
          <polygon points="4,4 11,0 18,4" fill="#fff"/>
        </svg>
        info@kttransport.example
      </div>
      <div class="contact-row" style="margin-top:14px">
        <svg width="22" height="22" viewBox="0 0 22 22" aria-hidden="true">
          <circle cx="11" cy="11" r="10.5" fill="#fff"/>
          <path d="M5 6c2-1 4 0 4 2s-3 2-2 5 3 2 3 5c-2 0-5-3-6-6s0-5 1-6zM13 4c2 0 5 2 5 5-1 1-3 0-3 2s2 3 1 5c-2 1-3-2-3-4s-2-2-1-4 1-3 1-4z" fill="#4a6479"/>
        </svg>
        www.ktvrx.example
      </div>
    </div>
    <div class="title-block">
      <div class="title-light">COMPANY</div>
      <div class="title-bold">INTRODUCTION</div>
    </div>
  </footer>

  <div class="watermark-clip" aria-hidden="true">
    <div class="watermark-name">K&amp;T</div>
  </div>
</main>
</body>
</html>
```